Flyer-Design für Überwachungskameras
Zielgruppe
wir sind eine kleine Firma die im Süd-Badischen Raum Sicherheitstechnik (Überwachungskameras, Alarmanlage, Türschließsysteme, Klingelanlagen) verbaut. Wir sind preislich hier in der Gegend unschlagbar, haben auch schon größere Kunden gehabt.
Auf unserer Seite ist ein Teil schon einsehbar. Ein erfolgreicher Flyer könnte zu einem Folgeauftrag zur Überarbeitung unserer Webseite führen.
Aufgabenstellung
Gewünscht ist ein Flyer den wir sowohl drucken lassen können zum verteilen aber auch online auf Plaudernetz (wir sind jetzt hier erst aktiv geworden, Spätsünder) platzieren können.
Der Flyer soll Kunden die gerade Überwachungskameras benötigen. Hier soll mit einspielen was alles möglich ist. Aktuelle Kameras mit KI die Mensch, Tier und Pkw unterscheiden können, Wärmebildkameras die Alarm geben können bei Hitze bzw Brandentstehung. Kameras verwenden wir die von 'Korvin' auf https://www.korvinoptik.example/de können sich hierzu kurze Information geholt werden. Hier sind auch bereits Flyer zum Download die jeweils Infos haben die wir nutzen dürfen. Auch das Bildmaterial. Desweiteren hat der Shop wachtrino.example auf seiner Seite auch einige Infos die wir ebenfalls nutzen dürfen.
Bezüglich Alarmanlagen, sind wir FERNO-Elektrotechnik zertifiziert. Haben Tremaro und Korvin im Potfolio auf weitere auf Anfrage.
Flyer sollte vielleicht max 4 Seiten haben. Wir sind aber für alles offen. Wenn er nur 2 hat und Top ist gut und wenn er 6 hat auch gut. Größe eventuell A5 aber auch hier setzen wir keine Grenzen und sind offen.

```html
<!DOCTYPE html>
<html lang="de">
<head>
<meta charset="utf-8">
<title>KL-VISTRA Sicherheitstechnik – Faltflyer</title>
<link rel="stylesheet" href="https://fonts.googleapis.com/css2?family=Bebas+Neue&family=Noto+Sans:wght@400;700&display=swap">
<style>
:root{
  --teal:#1f8fa3;
  --dark:#2a2a2a;
  --green:#6ab42d;
  --ink:#333;
  --paper:#ffffff;
  --stage:#e8e8e8;
  --display:'Bebas Neue', 'Oswald', sans-serif;
  --text:'Noto Sans', Arial, sans-serif;
}
*{box-sizing:border-box;margin:0;padding:0}
html,body{width:1200px;height:849px;overflow:hidden;background:var(--stage)}
.stage{position:relative;width:1200px;height:849px}
.spread{position:absolute;top:220px;width:580px;height:409px;background:var(--paper);
  box-shadow:0 2px 6px rgba(0,0,0,.25);overflow:hidden;font-family:var(--text);color:var(--ink)}
.spread--outside{left:10px}
.spread--inside{left:610px}
.panel{position:absolute;top:0;width:193.33px;height:409px;overflow:hidden}
.panel--1{left:0}.panel--2{left:193.33px}.panel--3{left:386.67px}

/* outside */
.photo{position:absolute;top:0;left:0;width:100%;height:179px}
.photo--relax-woman{background:linear-gradient(160deg,#b9b7b4,#8c8f93 55%,#6f7378)}
.photo--lens{background:linear-gradient(135deg,#2f5d78 0%,#1c2a33 45%,#7a4a22 75%,#3d6a85 100%)}
.photo--relax-man{background:linear-gradient(170deg,#e4e1dc,#b3b7bc 50%,#6c8aa8 85%)}
.ticker{position:absolute;top:179px;left:0;width:100%;height:26px;background:var(--dark);
  color:var(--green);font-family:var(--display);font-size:13.5px;line-height:26px;white-space:nowrap;letter-spacing:.2px}
.teal-field{position:absolute;top:205px;left:0;width:100%;height:204px;background:var(--teal)}
.teal-field svg{position:absolute;left:0;top:0}
.cover-headline{position:absolute;top:217px;font-family:var(--display);color:#fff;font-size:27px;line-height:26px;white-space:nowrap}
.panel--1 .cover-headline{left:-4px;text-align:left}
.panel--3 .cover-headline{left:49px}
.brand{display:flex;align-items:center;gap:4px}
.brand__dot{width:9px;height:9px;border-radius:50%;background:var(--teal)}
.brand__name{font-family:var(--text);font-weight:700;color:var(--green);font-size:13px;letter-spacing:.3px}
.brand__sub{font-size:6.5px;letter-spacing:.6px;color:#444;margin-left:13px}
.panel--1 .brand-block{position:absolute;left:28px;top:388px;transform:translateY(-100%)}
.icons{position:absolute;top:362px;left:18px;display:flex;gap:12px}
.icons svg{width:24px;height:22px}

.back{background:var(--paper);border-left:1px solid #eee;border-right:1px solid #eee}
.back__url{position:absolute;left:22px;top:385px;transform:rotate(-90deg);transform-origin:left top;
  font-family:var(--display);font-size:15px;color:var(--green);white-space:nowrap}
.back .brand-block{position:absolute;left:54px;top:278px}
.address{position:absolute;left:54px;top:333px;font-size:7.6px;line-height:11.6px;color:#333;font-style:normal}
.address strong{font-weight:700}

/* inside */
.claim-band{position:absolute;top:0;left:0;width:580px;height:25px;background:var(--dark);
  color:var(--green);font-family:var(--display);font-size:12.5px;letter-spacing:1.9px;line-height:25px;text-align:center;white-space:nowrap}
.inside-body{position:absolute;top:25px;left:0;width:580px;height:384px}
.intro{position:absolute;left:0;top:0;width:145px;height:384px;background:var(--teal);
  padding:18px 4px 0 20px;color:#fff;font-family:var(--display);font-size:18.5px;line-height:20.5px;white-space:nowrap}
.intro p + p{margin-top:20px}
.grid{position:absolute;left:145px;top:0;width:290px;height:384px;display:grid;
  grid-template-columns:1fr 1fr;grid-template-rows:repeat(3,1fr)}
.cell{padding:18px 8px 0 11px}
.cell h3{font-family:var(--display);font-weight:400;color:var(--green);font-size:9.5px;margin-bottom:4px}
.cell p{font-size:5.1px;line-height:8.9px;color:#444}
.product--thermal{background:radial-gradient(ellipse at 55% 55%,#fafafa 0 30%,#e2e2e2 70%)}
.product--domes{background:radial-gradient(ellipse at 50% 55%,#f6f6f6 0 30%,#dedede 75%)}
.product--ptz{background:radial-gradient(ellipse at 55% 60%,#f8f8f8 0 30%,#e0e0e0 75%)}
.about{position:absolute;left:435px;top:0;width:145px;height:384px;padding:17px 8px 0 14px}
.about p{font-size:9.2px;line-height:12.4px;font-weight:700;color:#333}
.about p + p{margin-top:10px}
.partners{position:absolute;left:449px;top:318px;display:flex;align-items:center;gap:22px}
.partners__badge{width:28px;height:28px;border-radius:50%;background:#e3a43a}
.partners__name{font-family:var(--text);font-weight:700;font-size:14px;color:#c8202f}
.about__url{position:absolute;left:449px;top:360px;font-family:var(--display);color:var(--green);font-size:15px;white-space:nowrap}
</style>
</head>
<body>
<main class="stage">

  <section class="spread spread--outside" aria-label="Außenseite">
    <div class="panel panel--1">
      <div class="photo photo--relax-woman" role="img" aria-label="Foto: entspannte Frau auf dem Sofa"></div>
      <div class="ticker" style="text-indent:-6px">LAGEN . VIDEOSPRECHANLAGEN</div>
      <div class="teal-field">
        <svg width="194" height="204" viewBox="0 0 194 204"><path d="M0 204 L0 96 Q110 86 194 134 L194 204 Z" fill="#fff"/></svg>
      </div>
      <div class="cover-headline">T ZU HABEN<br>ES GEFÜHL.</div>
      <div class="brand-block">
        <div class="brand"><span class="brand__dot"></span><span class="brand__name">KL-VISTRA</span></div>
        <div class="brand__sub">Sicherheitstechnik</div>
      </div>
    </div>

    <div class="panel panel--2 back">
      <div class="photo photo--lens" role="img" aria-label="Foto: Nahaufnahme eines Kameraobjektivs"></div>
      <div class="ticker" style="text-indent:12px">VIDEOÜBERWACHUNG . ALARMANLAGEN . VIDEOSPRECHANLAGEN</div>
      <div class="back__url">WWW.KL-VISTRA.EXAMPLE</div>
      <div class="brand-block">
        <div class="brand"><span class="brand__dot"></span><span class="brand__name">KL-VISTRA</span></div>
        <div class="brand__sub">Sicherheitstechnik</div>
      </div>
      <address class="address">
        <strong>Hain &amp; Barth GbR</strong><br>
        Feldweg 12<br>
        79999 Musterau<br>
        +49 7000 / 12 34 567<br>
        info@kl-vistra.example
      </address>
    </div>

    <div class="panel panel--3">
      <div class="photo photo--relax-man" role="img" aria-label="Foto: entspannter Mann auf dem Sofa"></div>
      <div class="ticker" style="text-indent:12px">VIDEOÜBERWACHUNG . ALARMANLAGEN</div>
      <div class="teal-field">
        <svg width="194" height="204" viewBox="0 0 194 204"><path d="M0 204 L0 134 Q84 86 194 96 L194 204 Z" fill="#fff"/></svg>
      </div>
      <div class="cover-headline">SICHERHEIT<br>IST EIN GUT</div>
      <div class="icons" aria-hidden="true">
        <svg viewBox="0 0 24 22" fill="none" stroke="#6ab42d" stroke-width="1.4"><path d="M2 4h20l-2 5H4z"/><path d="M5 9q0 9 7 9t7-9"/><circle cx="12" cy="12" r="3"/><circle cx="12" cy="12" r="1"/></svg>
        <svg viewBox="0 0 24 22" fill="none" stroke="#6ab42d" stroke-width="1.4"><path d="M6 16V10a6 6 0 0 1 12 0v6l2 2H4z"/><path d="M10 20a2 2 0 0 0 4 0"/><path d="M12 2v2"/></svg>
        <svg viewBox="0 0 24 22" fill="none" stroke="#6ab42d" stroke-width="1.4"><rect x="2" y="2" width="20" height="18"/><rect x="5" y="5" width="10" height="12"/><circle cx="10" cy="10" r="2"/><path d="M7 16q3-4 6 0"/><path d="M18 6v2M18 11v2M18 15v2"/></svg>
      </div>
    </div>
  </section>

  <section class="spread spread--inside" aria-label="Innenseite">
    <div class="claim-band">KL-VISTRA IST IHR SPEZIALIST FÜR ALARMANLAGEN, VIDEOÜBERWACHUNG UND SMARTHOME-TECHNIK.</div>
    <div class="inside-body">
      <div class="intro">
        <p>VERPIXELTE<br>BILDER?<br>VERGANGENHEIT.<br>HEUTE WIRD IN<br>4K-QUALITÄT<br>ÜBERWACHT.</p>
        <p>DANK NEUESTER<br>TECHNIK UND<br>EXPERTENBE-<br>RATUNG DAS ZU<br>ÜBERWACHENDE<br>OBJEKT JEDER-<br>ZEIT UND VON<br>ÜBERALL IM<br>BLICK HABEN.</p>
      </div>
      <div class="grid">
        <div class="cell">
          <h3>WÄRMEBILDKAMERAS</h3>
          <p>Wärmebildtechnik erkennt Personen auch bei völliger Dunkelheit und meldet ungewöhnliche Hitze sofort. So entdecken Sie Brandherde früh, schützen Gebäude, Lager und Freiflächen zuverlässig und erhalten Alarme direkt auf Ihr Smartphone.</p>
        </div>
        <div class="product product--thermal" role="img" aria-label="Produktfoto: Wärmebild- und Bullet-Kameras"></div>
        <div class="product product--domes" role="img" aria-label="Produktfoto: Dome- und Boxkameras"></div>
        <div class="cell">
          <h3>NETZWERK- UND IP-KAMERAS</h3>
          <p>Netzwerkkameras liefern gestochen scharfe Bilder in 4K. Intelligente Analyse unterscheidet Mensch, Tier und Fahrzeug, reduziert Fehlalarme deutlich und speichert Aufnahmen sicher auf Rekorder oder in der Cloud für spätere Auswertung.</p>
        </div>
        <div class="cell">
          <h3>FUNK- UND WLAN-KAMERAS</h3>
          <p>Funkkameras lassen sich ohne aufwendige Verkabelung montieren. Ideal für Altbauten, Gartenhäuser und Baustellen: schnell installiert, einfach per App eingerichtet und jederzeit von unterwegs abrufbar, ganz gleich wo Sie gerade sind.</p>
        </div>
        <div class="product product--ptz" role="img" aria-label="Produktfoto: Dome- und Schwenk-Neige-Kameras"></div>
      </div>
      <div class="about">
        <p>Sicherheit zu haben ist ein gutes Gefühl. In den privaten vier Wänden, sowie im geschäftlichen Umfeld.</p>
        <p>Mit unseren Kameras von KORVIN finden wir für Sie gemeinsam die passende Sicherheits­lösung.</p>
        <p>Wir beraten Sie von Anfang an völlig unverbindlich und unentgeltlich.</p>
        <p>Wir ermitteln Ihren Bedarf, erarbeiten ein optimales Sicherheits­konzept, besorgen die Hardware und nehmen alle Installationen vor.</p>
      </div>
      <div class="partners">
        <span class="partners__badge" role="img" aria-label="Zertifikat FERNO-Elektrotechnik"></span>
        <span class="partners__name">Korvin</span>
      </div>
      <div class="about__url">WWW.KL-VISTRA.EXAMPLE</div>
    </div>
  </section>

</main>
</body>
</html>
```